Custom Made Digital Jukebox sales and rental website

I need a design for a Custom Made Digital Jukebox sales and rental services website. Domain name is quelitrune.com. Exisiting customer shall have a section to register, login/logout, my account, support. All other visitor shall have at least the following options or menu avaialble: Home, FAQ, Services, Products, and Contact us. I have attached a high level requirements pdf file. Please don't be limited by high level requirements file attached, your idea may be better than what I specified. My products are designed base on customer requirements. Common parts are: Bill and Coin Acceptors, Touchscreen or keypad. All of them are wall mount.

Target Market(s)

Custom made digital Jukebox for Home and Commercial use

Industry/Entity Type

Digital

Number of Pages Required

1 page

Requirements
Must have
• PSD required.
Nice to have
• HTML code and CSS Stylesheet
• Logo for QueliTrune
• Inner Pages
Should not have
• Copyright material from related websites, previously developed or any other.

```html
<!DOCTYPE html>
<html lang="en">
<head>
<meta charset="utf-8">
<title>QueliTrune – Custom Made Digital Jukebox Sales &amp; Rental</title>
<link href="https://fonts.googleapis.com/css2?family=Open+Sans:wght@300;400;600;700;800&display=swap" rel="stylesheet">
<style>
:root{
  --ink:#111111;
  --night:#000000;
  --coal:#1b1b1b;
  --orange:#e8671a;
  --green:#7cc242;
  --linen:#d8d0bf;
  --cocoa:#4b3c2b;
  --paper:#ffffff;
  --mist:#e6e6e6;
  --grey:#888888;
  --text-dark:#222222;
}
*{margin:0;padding:0;box-sizing:border-box}
html,body{width:1200px;height:2695px;overflow:hidden}
body{font-family:"Open Sans",Arial,sans-serif;background:var(--ink);color:var(--paper);position:relative}
.abs{position:absolute}
a{color:inherit;text-decoration:none}

/* header */
.site-header{position:absolute;left:0;top:0;width:1200px;height:108px;background:var(--ink)}
.brand{left:97px;top:28px;font-size:40px;font-weight:800;letter-spacing:-0.5px;color:var(--paper);line-height:1}
.account-links{left:862px;top:18px;font-size:11px;letter-spacing:.3px;color:#cfcfcf;display:flex;gap:14px;align-items:center}
.account-links .sep{color:#777}
.login-btn{left:1035px;top:12px;width:66px;height:30px;background:var(--green);color:var(--paper);font-size:12px;font-weight:700;display:flex;align-items:center;justify-content:center}
.main-nav{left:744px;top:61px;display:flex;gap:20px;font-size:14px;font-weight:700;color:var(--paper)}

/* hero */
.hero{left:0;top:108px;width:1200px;height:562px;background:radial-gradient(ellipse at 50% 45%,#f7a02a 0%,#e2491a 35%,#a3170e 65%,#3a0806 100%)}
.hero-caption{left:0;top:540px;width:1200px;text-align:center;font-size:28px;font-weight:300;color:var(--paper);letter-spacing:-.3px}
.dots{display:flex;gap:8px}
.dots span{width:12px;height:12px;border-radius:50%;background:var(--paper)}
.dots span.on{background:var(--green)}
.hero-dots{left:563px;top:630px}

/* offer */
.offer{left:0;top:670px;width:1200px;height:362px;background:var(--night)}
.section-title{width:1200px;left:0;text-align:center;font-size:25px;font-weight:800;letter-spacing:-.3px}
.orange{color:var(--orange)}
.offer-img{top:763px;height:182px}
.offer-label{top:958px;font-size:14px;font-weight:600;color:var(--paper)}

/* products */
.products{left:0;top:1032px;width:1200px;height:648px;background:var(--linen)}
.product-card{top:1144px;width:276px;height:270px;background:var(--paper);display:flex;align-items:center;justify-content:center}
.product-shot{width:130px;height:230px;border-radius:65px 65px 10px 10px}
.product-name{top:1434px;font-size:20px;font-weight:800;color:var(--orange)}
.product-desc{top:1468px;width:270px;font-size:12.5px;line-height:19px;color:var(--text-dark)}
.product-price{top:1520px;font-size:30px;font-weight:300;color:var(--text-dark)}
.cart-btn{top:1569px;width:100px;height:25px;background:var(--night);color:var(--paper);font-size:8.5px;font-weight:700;display:flex;align-items:center;justify-content:center;letter-spacing:.2px}

/* how it works */
.how{left:0;top:1680px;width:1200px;height:548px;background:var(--cocoa)}
.video{left:180px;top:1771px;width:843px;height:419px;background:linear-gradient(125deg,#1a0c07 0%,#8c1a10 30%,#1c8f6c 55%,#b3290f 75%,#1a0c07 100%)}
.play{left:562px;top:1940px}

/* testimonials */
.testimonials{left:0;top:2228px;width:1200px;height:380px;background:var(--coal)}
.avatar{left:147px;top:2275px;width:230px;height:230px;border-radius:50%;border:5px solid var(--paper);background:radial-gradient(circle at 50% 40%,#a7a58a 0%,#6f7a4c 55%,#3d4a2c 100%)}
.quote-name{left:406px;top:2364px;font-size:14px;font-weight:800;color:var(--orange)}
.quote-text{left:406px;top:2410px;width:610px;font-size:13px;line-height:23.5px;color:#c9c9c9}
.testi-dots{left:563px;top:2564px}
.testi-dots span{width:11px;height:11px}
.testi-dots span.on{background:var(--orange)}

/* footer */
.site-footer{left:0;top:2608px;width:1200px;height:87px;background:var(--mist);color:var(--text-dark)}
.footer-nav{left:106px;top:2633px;display:flex;gap:10px;font-size:11.5px;font-weight:600}
.footer-nav .sep{color:#666}
.copyright{left:106px;top:2661px;font-size:11px;font-weight:600}
.footer-label{top:2643px;font-size:10.5px;font-weight:600}
.pay-name{left:736px;top:2636px;font-size:18px;font-weight:700;color:#2a3a6a}
.social{top:2638px;display:flex;align-items:center;gap:5px;font-size:11px;font-weight:600;color:#3b6fb0}
.social i{width:20px;height:20px;border-radius:50%;border:1.5px solid #3b6fb0;display:block}
</style>
</head>
<body>

<header class="site-header">
  <div class="abs brand">QueliTrune</div>
  <nav class="abs account-links"><a href="#">MY ACCOUNT</a><span class="sep">|</span><a href="#">SUPPORT</a></nav>
  <a class="abs login-btn" href="#">LOGIN</a>
  <nav class="abs main-nav"><a href="#">HOME</a><a href="#">FAQ</a><a href="#">SERVICES</a><a href="#">PRODUCTS</a><a href="#">CONTACT US</a></nav>
</header>

<section class="abs hero" role="img" aria-label="Glowing vintage jukebox with record stack"></section>
<p class="abs hero-caption">Custom Made Digital Jukebox Sales &amp; Rental Services</p>
<div class="abs dots hero-dots"><span class="on"></span><span></span><span></span><span></span><span></span></div>

<section class="abs offer"></section>
<h2 class="abs section-title orange" style="top:705px">WHAT WE OFFER</h2>
<div class="abs offer-img" style="left:98px;width:320px;background:linear-gradient(120deg,#3a0a05,#e0401a 45%,#f0a030 70%,#4a1208)" role="img" aria-label="Close-up of a lit jukebox front"></div>
<div class="abs offer-img" style="left:440px;width:318px;background:linear-gradient(160deg,#3a2a8a,#7a4ad0 35%,#1a0a20 60%,#6a1a10)" role="img" aria-label="Jukebox selector panel in blue light"></div>
<div class="abs offer-img" style="left:778px;width:320px;background:linear-gradient(120deg,#e8e8e8,#9a8a88 40%,#8a2a3a 70%,#3a2a2a)" role="img" aria-label="Friends dancing beside a jukebox"></div>
<p class="abs offer-label" style="left:98px">Easy Interface</p>
<p class="abs offer-label" style="left:440px">Enjoy Your Music</p>
<p class="abs offer-label" style="left:778px">Bestsound Quality</p>

<section class="abs products"></section>
<h2 class="abs section-title orange" style="top:1073px">OUR PRODUCTS</h2>

<div class="abs product-card" style="left:171px"><div class="product-shot" style="background:linear-gradient(90deg,#3a1a0a,#c0501a 30%,#e050c0 70%,#3a1a0a)" role="img" aria-label="Wooden jukebox with coloured light tubes"></div></div>
<div class="abs product-card" style="left:474px"><div class="product-shot" style="border-radius:14px;height:190px;background:linear-gradient(180deg,#e0501a,#c0201a 40%,#2a4ad0 80%,#1a1a2a)" role="img" aria-label="Compact jukebox with blue and red lights"></div></div>
<div class="abs product-card" style="left:778px"><div class="product-shot" style="background:linear-gradient(180deg,#f0a020,#e0601a 40%,#c0d020 70%,#2a1a0a)" role="img" aria-label="Classic arched jukebox in yellow and orange"></div></div>

<h3 class="abs product-name" style="left:173px">JUKEBOX 1</h3>
<h3 class="abs product-name" style="left:476px">JUKEBOX 1</h3>
<h3 class="abs product-name" style="left:780px">JUKEBOX 1</h3>
<p class="abs product-desc" style="left:171px">Neque porro quisquam est qui dolorem ipsum quia dolor sit amet, consectetur</p>
<p class="abs product-desc" style="left:474px">Neque porro quisquam est qui dolorem ipsum quia dolor sit amet, consectetur</p>
<p class="abs product-desc" style="left:779px">Neque porro quisquam est qui dolorem ipsum quia dolor sit amet, consectetur</p>
<p class="abs product-price" style="left:170px">$288.00</p>
<p class="abs product-price" style="left:473px">$288.00</p>
<p class="abs product-price" style="left:778px">$288.00</p>
<a class="abs cart-btn" style="left:169px" href="#">ADD TO CART</a>
<a class="abs cart-btn" style="left:472px" href="#">ADD TO CART</a>
<a class="abs cart-btn" style="left:778px" href="#">ADD TO CART</a>

<section class="abs how"></section>
<h2 class="abs section-title" style="top:1713px;color:var(--paper)">HOW IT WORKS</h2>
<div class="abs video" role="img" aria-label="Video still of illuminated jukebox selection buttons"></div>
<svg class="abs play" width="78" height="78" viewBox="0 0 78 78" aria-hidden="true">
  <circle cx="39" cy="39" r="36" fill="none" stroke="#ffffff" stroke-width="4"/>
  <polygon points="30,22 30,56 57,39" fill="#ffffff"/>
</svg>

<section class="abs testimonials"></section>
<h2 class="abs section-title" style="top:2263px;color:var(--paper)">CUSTOMER TESTIMONIALS</h2>
<div class="abs avatar" role="img" aria-label="Portrait of the customer"></div>
<h4 class="abs quote-name">DANIEL ORWICK</h4>
<p class="abs quote-text">Lorem Ipsum is simply dummy text of the printing and typesetting industry. Lorem Ipsum has been the industry's standard dummy text ever since the 1500s, when an unknown printer took a galley of type and scrambled it to make a type specimen book. It has survived not only five centuries, but also the leap into electronic typesetting</p>
<div class="abs dots testi-dots"><span class="on"></span><span></span><span></span><span></span></div>

<footer class="abs site-footer"></footer>
<nav class="abs footer-nav"><a href="#">HOME</a><span class="sep">|</span><a href="#">ABOUT US</a><span class="sep">|</span><a href="#">FAQ'S</a><span class="sep">|</span><a href="#">CONTACT US</a></nav>
<p class="abs copyright">© 2014 COMPANY NAME,ALL RIGHTS RESERVED</p>
<p class="abs footer-label" style="left:632px">PAYMENT OPTIONS</p>
<p class="abs pay-name">PayLumen</p>
<p class="abs footer-label" style="left:944px">CONNECT WITH US</p>
<div class="abs social" style="left:1045px;top:2629px"><i></i>Chirplet</div>
<div class="abs social" style="left:1045px;top:2655px"><i></i>Friendwall</div>

</body>
</html>
```